POLAR.MOTH snowsport and living

Polar Moth webpage design brief

Polar Moth is a life style brand
for those who love winter, snowboarding, and coffee.

We have log houses at some best snowboarding locations in Japan, in which easy and comfortable ambience make guests feel at home during their winter stay. Out there on the slopes, there are Polar Moth’s exclusive coffee kiosks that offer a wide selection of fine coffee from boutique roasters over the world to warm the hands and hearts of whenever our guests need!

Enjoy the snow with Polar Moth!

Tone & Manner: Simple, Tranquil, Relaxed, Enjoyable
 
Look and Feel : Monotone images of log house in the snowy winter and snowboarding people.  Capture of real-people-real-life moments. Red and blue colors can be used on icons and other vector elements in a much smaller scale in the overall picture.  Please refer to the attached color pallette.

Mainly informational with links to Stayvora for booking
Social media registration pass over from talkpin. Mixaroo or Stayvora
Recruitment link to Workbeam

Currently I do not have any pictures. So need a bit of discussion on this area.

Also the website needs to be in 3 languages, English, Chinese and Japanese.

Rough Sitemap:

Home (language selection on every page)
About
GO (snow villas)
Coffee (coffee kiosks on slopes)
Reservations

(Bottom of screen)
Contact us
Company info
Recruit

Reference website:
Quenlodge.com
Tarudome.co.jp

Attached pictures are for references not for use!!!
Color reference pls refer to attached file 4.
Updates

Reason: More updates on project briefs. Please have a look.

Target Market(s)

Snowboarders

Industry/Entity Type

Hospitality

Number of Pages Required

5+ page

Font styles to use
Sans Serif

Colors

Designer to choose colors to be used in the design.

Requirements
Must have
• Mobile version
• 3 languages
• Registration thru TalkPin, Mixaroo or Stayvora
Nice to have
• Illustration instead of pictures

```html
<!DOCTYPE html>
<html lang="en">
<head>
<meta charset="utf-8">
<title>Polar Moth – Snowsport and Living</title>
<link href="https://fonts.googleapis.com/css2?family=Lato:wght@300;400;700;900&family=Open+Sans:wght@400;600;700&display=swap" rel="stylesheet">
<style>
:root{
  --sky:#6d8fb1;
  --sky-deep:#5f81a4;
  --snow:#f4f7fa;
  --snow-blue:#c9d8e7;
  --navy:#363d52;
  --navy-soft:#454c63;
  --ink:#2b2f3a;
  --text:#3a3d45;
  --line:#d6d8dc;
  --red:#c0392b;
  --rule:#8c3a44;
  --coral:#f45b60;
  --field:#a7a8ae;
  --black:#0c0c0e;
  --blue:#2376b7;
  --white:#ffffff;
}
*{box-sizing:border-box;margin:0;padding:0}
html,body{width:1200px;height:3010px;overflow:hidden}
body{position:relative;font-family:"Open Sans",Arial,sans-serif;color:var(--text);background:var(--white)}
a{text-decoration:none}
.abs{position:absolute}

/* hero */
.hero{left:0;top:0;width:1200px;height:565px;background:linear-gradient(180deg,var(--sky) 0%,var(--sky-deep) 100%);overflow:hidden}
.hero-hills{left:0;top:0;width:1200px;height:565px}
.hero-figure{left:170px;top:200px;width:210px;height:230px;background:radial-gradient(ellipse at 50% 50%,rgba(255,255,255,.55) 0%,rgba(255,255,255,.18) 45%,rgba(255,255,255,0) 70%)}
.hero-cabin{left:940px;top:300px;width:260px;height:240px;background:radial-gradient(ellipse at 55% 60%,rgba(255,255,255,.6) 0%,rgba(255,255,255,.2) 45%,rgba(255,255,255,0) 72%)}
.nav-bar{left:0;top:0;width:1200px;height:69px;border-bottom:1px solid rgba(255,255,255,.5)}
.brand{left:128px;top:12px;font-family:"Lato",sans-serif;font-weight:700;font-size:34px;color:var(--white)}
.nav{top:23px;font-size:16px;color:var(--white)}
.lang-flag{left:1018px;top:21px;width:58px;height:30px;background:linear-gradient(90deg,#2a3f7a 0%,#2a3f7a 40%,#c7303f 100%);border:1px solid var(--white)}
.lang-caret{left:1086px;top:25px;width:20px;height:20px;background:var(--white)}
.lang-caret::after{content:"";position:absolute;left:5px;top:7px;border-left:5px solid transparent;border-right:5px solid transparent;border-top:6px solid var(--navy)}
.hero-title{left:0;top:152px;width:1200px;text-align:center;font-family:"Lato",sans-serif;font-weight:400;font-size:32px;color:var(--white)}
.hero-copy{left:330px;top:203px;width:540px;text-align:center;font-size:15px;line-height:27px;color:var(--white)}
.btn-ghost{left:496px;top:290px;width:208px;height:42px;border:1px solid var(--white);color:var(--white);font-size:15px;text-align:center;line-height:40px}
.hero-rule{left:0;top:565px;width:1200px;height:3px;background:var(--rule)}

/* shared */
.frame{border:1px solid var(--line)}
.photo{box-shadow:0 2px 6px rgba(0,0,0,.28)}
.section-title{font-family:"Lato",sans-serif;font-weight:300;font-size:32px;color:var(--ink)}
.body-copy{font-size:15px;line-height:26.5px;color:var(--text)}
.btn-dark{background:var(--navy);color:var(--white);font-size:15px;text-align:center}
.band-dark{left:0;width:1200px}
.band-title{left:0;width:1200px;text-align:center;font-family:"Lato",sans-serif;font-weight:400;font-size:32px;color:var(--white)}

/* intro */
.intro-mark{left:820px;top:600px;width:240px;height:300px;background:radial-gradient(ellipse at 50% 50%,rgba(200,200,200,.35) 0%,rgba(200,200,200,0) 70%)}

/* reservation */
.field-label{font-size:15px;color:var(--white)}
.field{height:42px;background:var(--field);color:var(--white);font-size:13px;line-height:42px;padding-left:16px}
.field-icon{position:absolute;right:14px;top:14px;width:14px;height:14px}
.book-btn{left:786px;top:1184px;width:324px;height:42px;background:var(--coral);border:1px solid var(--white);color:var(--white);font-size:15px;line-height:40px}
.book-btn .label{position:absolute;left:80px}
.book-btn .divider{position:absolute;left:176px;top:8px;width:1px;height:24px;background:var(--white)}
.book-btn .partner{position:absolute;left:190px;font-weight:600}

/* gallery */
.card-photo{border:3px solid #dcdde0;box-shadow:0 1px 4px rgba(0,0,0,.3)}
.card-caption{font-size:12px;color:var(--ink)}
.card-link{font-size:12px;color:var(--red)}

/* services */
.service-box{width:324px;height:144px;border:1px solid var(--white);color:var(--white);font-size:14px;line-height:21px;text-align:center;padding:38px 28px 0}
.service-icon{width:60px;height:64px}

/* testimonial */
.quote-box{left:174px;top:2612px;width:852px;height:156px;border:1px solid var(--white)}
.quote-head{left:516px;top:2596px;width:168px;height:32px;background:#3d4459;color:var(--white);font-weight:700;font-size:15px;line-height:32px;text-align:center}
.quote-mark{font-family:"Lato",sans-serif;font-weight:900;font-size:44px;vertical-align:-18px;margin-right:10px}
.avatar{left:226px;top:2654px;width:76px;height:76px;border-radius:50%;background:radial-gradient(circle at 50% 45%,#e9874a 0%,#c65a24 70%,#a8441a 100%)}
.quote-copy{left:340px;top:2646px;width:676px;font-size:15px;line-height:24.7px;color:var(--white)}
.arrow-btn{top:2788px;width:28px;height:28px}

/* footer */
.footer{left:0;top:2856px;width:1200px;height:154px;background:var(--black)}
.footer-link{top:2887px;font-size:15px;color:var(--white)}
.footer-sep{top:2884px;width:1px;height:28px;background:#555}
.footer-rule{left:0;top:2930px;width:1200px;height:1px;background:#333}
.social{top:2942px;height:46px;display:flex;align-items:center;gap:7px;color:var(--white);font-size:13px;font-weight:600}
.social .sq{width:22px;height:22px;background:#4a4f5c}
.copyright{left:0;top:2957px;width:1200px;text-align:center;font-size:12px;color:var(--white)}
.recruit-btn{left:934px;top:2940px;width:178px;height:46px;background:var(--blue);color:var(--white);font-size:15px;line-height:46px}
.recruit-btn .label{position:absolute;left:14px}
.recruit-btn .divider{position:absolute;left:114px;top:0;width:2px;height:24px;background:var(--white)}
.recruit-btn .partner{position:absolute;left:122px;font-weight:700;font-size:12px}
</style>
</head>
<body>

<!-- Hero -->
<section class="abs hero">
  <svg class="abs hero-hills" viewBox="0 0 1200 565" aria-hidden="true">
    <path d="M0 330 C120 360 230 400 330 430 C420 455 480 470 560 488 C700 500 820 498 900 500 C1000 520 1100 545 1200 560 L1200 565 L0 565Z" fill="#c8d7e6"/>
    <path d="M300 420 C360 430 430 440 500 470 C580 492 700 492 820 494 C930 500 1060 530 1200 552 L1200 565 L0 565 L0 500 C120 470 220 440 300 420Z" fill="#e6edf4"/>
    <path d="M0 520 C200 500 420 500 620 520 C820 535 1020 548 1200 556 L1200 565 L0 565Z" fill="#f6f8fb"/>
  </svg>
  <div class="abs hero-figure" role="img" aria-label="Illustration of a snowboarder jumping off a slope"></div>
  <div class="abs hero-cabin" role="img" aria-label="Illustration of snowy pine trees around a log cabin"></div>
  <header class="abs nav-bar">
    <div class="abs brand">Polar Moth</div>
    <nav>
      <a class="abs nav" style="left:401px">Home</a>
      <a class="abs nav" style="left:522px">About</a>
      <a class="abs nav" style="left:645px">GO</a>
      <a class="abs nav" style="left:745px">Coffee</a>
      <a class="abs nav" style="left:870px">Reservations</a>
    </nav>
    <div class="abs lang-flag" role="img" aria-label="English language flag"></div>
    <div class="abs lang-caret"></div>
  </header>
  <h1 class="abs hero-title">Lorem Ipsum is simply</h1>
  <p class="abs hero-copy">Lorem Ipsum is simply dummy text of the printing and typesetting industry. Lorem Ipsum has been the industry's standard dummy text</p>
  <a class="abs btn-ghost">Read More</a>
</section>
<div class="abs hero-rule"></div>

<!-- Intro -->
<section>
  <div class="abs intro-mark" role="img" aria-label="Faint snowboarder decoration"></div>
  <div class="abs frame" style="left:146px;top:610px;width:290px;height:312px"></div>
  <div class="abs photo" role="img" aria-label="Photo of a snowboarder in pink and teal carving through powder snow" style="left:86px;top:622px;width:338px;height:290px;background:linear-gradient(165deg,#5d6f84 0%,#9fb4c9 18%,#dfe6ee 38%,#c96a8a 52%,#3aa6a8 62%,#eef1f5 78%,#d8dde4 100%)"></div>
  <h2 class="abs section-title" style="left:496px;top:618px">Lorem Ipsum is simply</h2>
  <p class="abs body-copy" style="left:498px;top:670px;width:612px">Lorem Ipsum is simply dummy text of the printing and typesetting industry. Lorem Ipsum has been the industry's standard dummy text ever since the 1500s, when an unknown printer took a galley of type and scrambled it to make a type specimen book. It has survived not only five centuries, but also the leap into electronic typesetting, remaining essentially unchanged. It was popularised in the 1960s with the release of Letraset.</p>
  <a class="abs btn-dark" style="left:498px;top:848px;width:114px;height:40px;line-height:40px">Read More</a>
</section>

<!-- Reservation -->
<section class="abs band-dark" role="img" aria-label="Faded photo of a snowy pine forest" style="top:966px;height:302px;background:linear-gradient(180deg,#4b536b 0%,#3f475e 45%,#394057 100%)"></section>
<h2 class="abs band-title" style="top:996px">Make a Reservations</h2>
<div class="abs field-label" style="left:86px;top:1064px">Check In</div>
<div class="abs field-label" style="left:436px;top:1064px">Check Out</div>
<div class="abs field-label" style="left:786px;top:1064px">Adult</div>
<div class="abs field" style="left:86px;top:1092px;width:324px">00/00/00
  <svg class="field-icon" viewBox="0 0 14 14"><rect x="1" y="2" width="12" height="11" fill="none" stroke="#fff" stroke-width="1.5"/><line x1="1" y1="5" x2="13" y2="5" stroke="#fff" stroke-width="1.5"/></svg></div>
<div class="abs field" style="left:436px;top:1092px;width:324px">00/00/00
  <svg class="field-icon" viewBox="0 0 14 14"><rect x="1" y="2" width="12" height="11" fill="none" stroke="#fff" stroke-width="1.5"/><line x1="1" y1="5" x2="13" y2="5" stroke="#fff" stroke-width="1.5"/></svg></div>
<div class="abs field" style="left:786px;top:1092px;width:324px">00
  <svg class="field-icon" viewBox="0 0 14 14"><path d="M3 6 L7 2 L11 6Z M3 8 L7 12 L11 8Z" fill="#fff"/></svg></div>
<div class="abs field-label" style="left:86px;top:1156px">Children</div>
<div class="abs field-label" style="left:436px;top:1156px">Room</div>
<div class="abs field" style="left:86px;top:1184px;width:324px">00
  <svg class="field-icon" viewBox="0 0 14 14"><path d="M3 6 L7 2 L11 6Z M3 8 L7 12 L11 8Z" fill="#fff"/></svg></div>
<div class="abs field" style="left:436px;top:1184px;width:324px">00/00/00
  <svg class="field-icon" viewBox="0 0 14 14"><rect x="1" y="2" width="12" height="11" fill="none" stroke="#fff" stroke-width="1.5"/><line x1="1" y1="5" x2="13" y2="5" stroke="#fff" stroke-width="1.5"/></svg></div>
<a class="abs book-btn"><span class="label">Book Now</span><span class="divider"></span><span class="partner">Stayvora</span></a>

<!-- Gallery -->
<section>
  <div class="abs card-photo" role="img" aria-label="Photo of a wooden log house with a thick snow roof among pines" style="left:86px;top:1310px;width:322px;height:246px;background:linear-gradient(180deg,#3c3e40 0%,#6f7276 14%,#eef1f4 30%,#f6f7f9 40%,#6b5140 52%,#4a372b 70%,#e9ecef 84%,#f7f8fa 100%)"></div>
  <div class="abs card-caption" style="left:100px;top:1561px">Log Houses</div>
  <div class="abs card-link" style="left:326px;top:1561px">View Details</div>
  <div class="abs card-photo" role="img" aria-label="Photo of a snowboarder in blue and yellow mid-air against a blue sky" style="left:436px;top:1310px;width:324px;height:246px;background:linear-gradient(180deg,#2f5f9c 0%,#4d7fbb 30%,#7aa2cf 52%,#3a4a36 62%,#dfe7ef 76%,#f3f6f9 100%)"></div>
  <div class="abs card-caption" style="left:450px;top:1561px">Snow Boarding</div>
  <div class="abs card-link" style="left:676px;top:1561px">View Details</div>
  <div class="abs card-photo" role="img" aria-label="Photo of coffee pouring into a white cup beside beans and croissants" style="left:788px;top:1310px;width:322px;height:246px;background:radial-gradient(ellipse at 50% 78%,#f3ede6 0%,#d9c7b4 14%,#7a4322 32%,#3b2116 58%,#1f130d 100%)"></div>
  <div class="abs card-caption" style="left:800px;top:1561px">Coffee</div>
  <div class="abs card-link" style="left:1026px;top:1561px">View Details</div>
</section>

<!-- Services -->
<section class="abs band-dark" role="img" aria-label="Faded photo of skiers on a snowy slope" style="top:1618px;height:494px;background:linear-gradient(180deg,#4f5770 0%,#4a5169 40%,#545a6e 62%,#464d63 100%)"></section>
<h2 class="abs band-title" style="top:1634px;font-size:30px">Our Services</h2>

<div class="abs service-box" style="left:86px;top:1730px">Lorem Ipsum is simply dummy text of the printing and typesetting industry. Lorem Ipsum has been the industry's standard dummy text.</div>
<div class="abs service-box" style="left:436px;top:1730px">Lorem Ipsum is simply dummy text of the printing and typesetting industry. Lorem Ipsum has been the industry's standard dummy text.</div>
<div class="abs service-box" style="left:786px;top:1730px">Lorem Ipsum is simply dummy text of the printing and typesetting industry. Lorem Ipsum has been the industry's standard dummy text.</div>
<div class="abs service-box" style="left:86px;top:1928px">Lorem Ipsum is simply dummy text of the printing and typesetting industry. Lorem Ipsum has been the industry's standard dummy text.</div>
<div class="abs service-box" style="left:436px;top:1928px">Lorem Ipsum is simply dummy text of the printing and typesetting industry. Lorem Ipsum has been the industry's standard dummy text.</div>
<div class="abs service-box" style="left:786px;top:1928px">Lorem Ipsum is simply dummy text of the printing and typesetting industry. Lorem Ipsum has been the industry's standard dummy text.</div>

<svg class="abs service-icon" style="left:218px;top:1698px" viewBox="0 0 60 64"><path d="M30 2 L57 17 L57 47 L30 62 L3 47 L3 17Z" fill="#fff"/><path d="M30 6 L53 19 L53 45 L30 58 L7 45 L7 19Z" fill="#3d465e"/><path d="M30 16 L33 28 L44 34 L44 37 L33 34 L32 44 L36 47 L36 49 L30 47 L24 49 L24 47 L28 44 L27 34 L16 37 L16 34 L27 28Z" fill="#fff"/></svg>
<svg class="abs service-icon" style="left:568px;top:1698px" viewBox="0 0 60 64"><path d="M30 2 L57 17 L57 47 L30 62 L3 47 L3 17Z" fill="#fff"/><path d="M30 6 L53 19 L53 45 L30 58 L7 45 L7 19Z" fill="#3d465e"/><g fill="#fff"><rect x="19" y="20" width="22" height="5" rx="2"/><rect x="19" y="27" width="22" height="5" rx="2"/><rect x="19" y="34" width="22" height="5" rx="2"/><rect x="19" y="41" width="22" height="5" rx="2"/></g></svg>
<svg class="abs service-icon" style="left:918px;top:1698px" viewBox="0 0 60 64"><path d="M30 2 L57 17 L57 47 L30 62 L3 47 L3 17Z" fill="#fff"/><path d="M30 6 L53 19 L53 45 L30 58 L7 45 L7 19Z" fill="#3d465e"/><g fill="none" stroke="#fff" stroke-width="2"><circle cx="30" cy="32" r="13"/><ellipse cx="30" cy="32" rx="6" ry="13"/><line x1="17" y1="32" x2="43" y2="32"/><line x1="19" y1="25" x2="41" y2="25"/><line x1="19" y1="39" x2="41" y2="39"/></g></svg>
<svg class="abs service-icon" style="left:218px;top:1896px" viewBox="0 0 60 64"><path d="M30 2 L57 17 L57 47 L30 62 L3 47 L3 17Z" fill="#fff"/><path d="M30 6 L53 19 L53 45 L30 58 L7 45 L7 19Z" fill="#3d465e"/><path d="M19 32 L27 40 L42 24" fill="none" stroke="#fff" stroke-width="4"/></svg>
<svg class="abs service-icon" style="left:568px;top:1896px" viewBox="0 0 60 64"><path d="M30 2 L57 17 L57 47 L30 62 L3 47 L3 17Z" fill="#fff"/><path d="M30 6 L53 19 L53 45 L30 58 L7 45 L7 19Z" fill="#3d465e"/><path d="M16 32 L44 20 L38 46 L30 38 Z M30 38 L28 46 L33 41" fill="none" stroke="#fff" stroke-width="2.2" stroke-linejoin="round"/></svg>
<svg class="abs service-icon" style="left:918px;top:1896px" viewBox="0 0 60 64"><path d="M30 2 L57 17 L57 47 L30 62 L3 47 L3 17Z" fill="#fff"/><path d="M30 6 L53 19 L53 45 L30 58 L7 45 L7 19Z" fill="#3d465e"/><rect x="16" y="20" width="28" height="19" fill="none" stroke="#fff" stroke-width="2.5"/><rect x="27" y="39" width="6" height="5" fill="#fff"/><rect x="22" y="44" width="16" height="3" fill="#fff"/></svg>

<!-- About -->
<section>
  <h2 class="abs section-title" style="left:84px;top:2146px">Lorem Ipsum is simply</h2>
  <p class="abs body-copy" style="left:84px;top:2206px;width:530px">Lorem Ipsum is simply dummy text of the printing and typesetting industry. Lorem Ipsum has been the industry's standard dummy text ever since the 1500s, when an unknown printer took a galley of type and scrambled it to make a type specimen book. It has survived not only five centuries, but also the leap into electronic typesetting, remaining essentially unchanged. It was popularised in the 1960s with the release of Letraset.</p>
  <a class="abs btn-dark" style="left:86px;top:2428px;width:114px;height:38px;line-height:38px">Read More</a>
  <div class="abs frame" style="left:674px;top:2154px;width:408px;height:310px;border-color:#9a9da4"></div>
  <div class="abs photo" role="img" aria-label="Photo of a red wooden chalet under snow among tall pine trees" style="left:700px;top:2172px;width:414px;height:272px;background:linear-gradient(180deg,#2f3a33 0%,#55645a 14%,#dfe4e9 28%,#f2f4f6 34%,#8a3a30 46%,#6e2c25 58%,#7a7570 68%,#dfe6ee 78%,#f6f8fa 100%)"></div>
</section>

<!-- Testimonials -->
<section class="abs band-dark" role="img" aria-label="Faded photo of a snowy pine forest" style="top:2508px;height:348px;background:linear-gradient(180deg,#4c536b 0%,#40475e 45%,#343b50 100%)"></section>
<h2 class="abs band-title" style="top:2538px;font-size:32px;font-weight:300">Testimonials</h2>
<div class="abs quote-box"></div>
<div class="abs quote-head"><span class="quote-mark">&ldquo;</span>John Doe</div>
<div class="abs avatar" role="img" aria-label="Guest portrait"></div>
<p class="abs quote-copy">Lorem Ipsum is simply dummy text of the printing and typesetting industry. Lorem Ipsum has been the industry's standard dummy text ever since the 1500s, when an unknown printer took a galley of type and scrambled it to make a type specimen book. It has survived not only five centuries Loreting industrturies .</p>
<svg class="abs arrow-btn" style="left:566px" viewBox="0 0 28 28"><rect width="28" height="28" fill="#fff"/><path d="M17 7 L10 14 L17 21" fill="none" stroke="#111" stroke-width="3"/></svg>
<svg class="abs arrow-btn" style="left:602px" viewBox="0 0 28 28"><rect width="28" height="28" fill="#fff"/><path d="M11 7 L18 14 L11 21" fill="none" stroke="#111" stroke-width="3"/></svg>

<!-- Footer -->
<footer class="abs footer"></footer>
<a class="abs footer-link" style="left:422px">Contact us</a>
<span class="abs footer-sep" style="left:532px"></span>
<a class="abs footer-link" style="left:556px">Company info</a>
<span class="abs footer-sep" style="left:694px"></span>
<a class="abs footer-link" style="left:722px">Recruit</a>
<div class="abs footer-rule"></div>
<a class="abs social" style="left:86px"><span class="sq"></span>TalkPin</a>
<a class="abs social" style="left:176px"><span class="sq"></span>Stayvora</a>
<a class="abs social" style="left:274px"><span class="sq"></span>Mixaroo</a>
<div class="abs copyright">Copyright@2017 &nbsp;Powered by Polarmoth.com</div>
<a class="abs recruit-btn"><span class="label">Recruitment</span><span class="divider"></span><span class="partner">Workbeam</span></a>

</body>
</html>
```